New Business and Accounting Software need a Graphics

We need graphic designs for a Business and Accounting Software that has 3 products and several modules.
Each product and module has its owns logo and color, when you do the design have in consideration that we are looking the experience that when you change from one product design to another the look and feel adjust to the color and logo of the product.
I am attaching:
1. Main Logo
2. Logos
3. Word Documents
You are welcome to use other icons for the each product if you want.
Target Market(s)
Independent profesional and Small and Medium Companies
Industry/Entity Type
Business and Accounting Softwares
Look and feel
Each slider illustrates characteristics of the customer's brand and the style your logo design should communicate.

```html
<!DOCTYPE html>
<html lang="es">
<head>
<meta charset="utf-8">
<title>Orbita – Productos y Módulos</title>
<link href="https://fonts.googleapis.com/css2?family=Poppins:wght@400;500;700;800&display=swap" rel="stylesheet">
<style>
  :root{
    --stage:#1e1f26;
    --white:#ffffff;
    --ink:#2b2b33;
    --brand:#0b5fb0;
    --finance-a:#1a7fd0;
    --finance-b:#0a4ea6;
    --people-a:#79c8c2;
    --people-b:#7bb88f;
    --crm-a:#7d76e0;
    --crm-b:#6a6ca6;
    --pill-deep:#0868b4;
    --pill-bright:#0a90e2;
    --pill-soft:#7daed8;
    --icon-teal:#72c0b0;
    --icon-yellow:#f3bf2f;
    --icon-orange:#f4693a;
    --icon-violet:#6a5ee8;
    --icon-sky:#8cc7f1;
    --line:#1469b8;
    --photo-a:#e8ddd0;
    --photo-b:#5e7d9e;
    --photo-c:#2a2f3a;
  }
  *{box-sizing:border-box;margin:0;padding:0}
  html,body{width:1200px;height:1140px;overflow:hidden;background:var(--stage);font-family:'Poppins',sans-serif}
  .slide{position:absolute;left:24px;width:1152px;height:540px;overflow:hidden;background:var(--white)}
  .slide--products{top:21px}
  .slide--modules{top:583px}
  .photo{position:absolute;inset:0;background:linear-gradient(125deg,var(--photo-a) 0%,#b9c4cf 30%,var(--photo-b) 55%,var(--photo-c) 80%,#c7d6e3 100%)}
  .art{position:absolute;inset:0;width:1152px;height:540px}
  .brand-name{font-family:'Poppins',sans-serif;font-weight:700;fill:var(--brand)}
  .card-label{font-family:'Poppins',sans-serif;font-weight:700;fill:#3a3a40;text-anchor:middle;letter-spacing:.5px}
  .numeral{font-family:'Poppins',sans-serif;font-weight:800}
  .menu{position:absolute;left:906px;top:26px;color:var(--ink)}
  .menu h2{font-size:18px;font-weight:700;color:var(--finance-a);letter-spacing:.5px;margin-bottom:4px}
  .menu ul{list-style:none}
  .menu li{font-size:13.4px;line-height:22.8px;padding-left:22px;position:relative;letter-spacing:.3px}
  .menu li::before{content:"›";position:absolute;left:0;top:-1px;font-weight:700;font-size:16px}
  .menu li.is-active{color:var(--finance-a);text-decoration:underline;text-underline-offset:3px}
  .module{position:absolute;width:434px;height:85px;border-radius:43px;color:var(--white);display:flex;align-items:center;padding:0 20px 0 10px}
  .module--deep{background:var(--pill-deep)}
  .module--bright{background:var(--pill-bright)}
  .module--soft{background:var(--pill-soft)}
  .module__icon{flex:none;width:70px;height:70px;border-radius:50%;display:flex;align-items:center;justify-content:center;margin-right:14px}
  .module__icon svg{width:44px;height:44px}
  .module h3{font-size:17px;font-weight:700;line-height:20px;letter-spacing:.3px}
  .module p{font-size:10px;line-height:16px;font-weight:500;letter-spacing:.2px}
</style>
</head>
<body>

<!-- Products slide -->
<section class="slide slide--products">
  <div class="photo" role="img" aria-label="Fotografía de una mano con bolígrafo revisando gráficos financieros impresos sobre un escritorio"></div>
  <svg class="art" viewBox="0 0 1152 540">
    <defs>
      <linearGradient id="gFinance" x1="0" y1="0" x2="0" y2="1"><stop offset="0" stop-color="var(--finance-a)"/><stop offset="1" stop-color="var(--finance-b)"/></linearGradient>
      <linearGradient id="gPeople" x1="0" y1="0" x2="0" y2="1"><stop offset="0" stop-color="var(--people-a)"/><stop offset="1" stop-color="var(--people-b)"/></linearGradient>
      <linearGradient id="gCrm" x1="0" y1="0" x2="0" y2="1"><stop offset="0" stop-color="var(--crm-a)"/><stop offset="1" stop-color="var(--crm-b)"/></linearGradient>
      <filter id="soft" x="-20%" y="-20%" width="140%" height="140%"><feDropShadow dx="0" dy="2" stdDeviation="3" flood-color="#000" flood-opacity=".18"/></filter>
    </defs>
    <path d="M583,0 Q389,270 583,540 L1152,540 L1152,0 Z" fill="var(--white)"/>

    <!-- connectors -->
    <g fill="none" stroke="var(--line)" stroke-width="2">
      <polyline points="520,176 541,140 623,140"/>
      <line x1="576" y1="275" x2="623" y2="275"/>
      <polyline points="520,365 541,401 599,401"/>
    </g>

    <!-- hub -->
    <rect x="392" y="178" width="182" height="184" rx="14" fill="#e6ebf2"/>
    <rect x="405" y="191" width="156" height="158" rx="10" fill="var(--white)" filter="url(#soft)"/>
    <circle cx="433" cy="270" r="8" fill="var(--brand)"/>
    <text class="brand-name" x="448" y="279" font-size="25">Orbita</text>

    <!-- numerals -->
    <text class="numeral" x="718" y="173" font-size="190" text-anchor="end" fill="url(#gFinance)">1</text>
    <text class="numeral" x="725" y="343" font-size="200" text-anchor="end" fill="url(#gPeople)">2</text>
    <text class="numeral" x="725" y="518" font-size="195" text-anchor="end" fill="url(#gCrm)">3</text>

    <!-- product 1 -->
    <rect x="705" y="27" width="153" height="146" rx="10" fill="url(#gFinance)"/>
    <path d="M858,64 L869,75 L858,86 Z" fill="var(--finance-a)"/>
    <rect x="717" y="38" width="131" height="123" rx="7" fill="var(--white)" filter="url(#soft)"/>
    <g fill="var(--finance-b)">
      <rect x="752" y="57" width="5" height="43"/><rect x="752" y="95" width="60" height="5"/>
      <rect x="762" y="80" width="6" height="12"/><rect x="772" y="72" width="6" height="20"/>
      <rect x="782" y="62" width="6" height="30"/><rect x="792" y="68" width="6" height="24"/>
      <rect x="802" y="58" width="6" height="34"/>
    </g>
    <text class="card-label" x="782" y="134" font-size="19">FINANZAS</text>

    <!-- product 2 -->
    <rect x="705" y="196" width="153" height="147" rx="10" fill="url(#gPeople)"/>
    <rect x="717" y="208" width="131" height="123" rx="7" fill="var(--white)" filter="url(#soft)"/>
    <g fill="var(--people-b)">
      <circle cx="782" cy="226" r="11"/><path d="M765,262 q0,-22 17,-22 q17,0 17,22 z"/>
      <circle cx="762" cy="234" r="7"/><path d="M751,259 q0,-15 11,-15 q9,0 10,8 l-4,7 z"/>
      <circle cx="802" cy="234" r="7"/><path d="M813,259 q0,-15 -11,-15 q-9,0 -10,8 l4,7 z"/>
    </g>
    <text class="card-label" x="782" y="290" font-size="19">HUMANOS</text>
    <text class="card-label" x="782" y="314" font-size="19">RECURSOS</text>

    <!-- product 3 -->
    <rect x="705" y="371" width="153" height="147" rx="10" fill="url(#gCrm)"/>
    <rect x="717" y="383" width="131" height="123" rx="7" fill="var(--white)" filter="url(#soft)"/>
    <g fill="var(--crm-a)">
      <ellipse cx="782" cy="404" rx="26" ry="8"/>
      <path d="M756,410 q26,12 52,0 v10 q-26,12 -52,0 z"/>
      <path d="M756,425 q26,12 52,0 v10 q-26,12 -52,0 z" fill="var(--crm-b)"/>
      <path d="M756,440 q26,12 52,0 v8 q-26,12 -52,0 z" fill="var(--crm-b)"/>
    </g>
    <text class="card-label" x="782" y="486" font-size="19">CRM</text>
  </svg>

  <nav class="menu">
    <h2>FINANZAS</h2>
    <ul>
      <li>Facturacion Electrónica</li>
      <li>Ventas</li>
      <li class="is-active">Compras</li>
      <li>Inventarios</li>
      <li>Contabilidad</li>
      <li>Bancos</li>
      <li>Presupuesto</li>
      <li>Tareas</li>
    </ul>
  </nav>
</section>

<!-- HR modules slide -->
<section class="slide slide--modules">
  <div class="photo" role="img" aria-label="Fotografía de una mano con bolígrafo revisando gráficos financieros impresos sobre un escritorio"></div>
  <svg class="art" viewBox="0 0 1152 540">
    <defs>
      <filter id="soft2" x="-20%" y="-20%" width="140%" height="140%"><feDropShadow dx="0" dy="2" stdDeviation="4" flood-color="#000" flood-opacity=".15"/></filter>
    </defs>
    <path d="M583,0 Q389,270 583,540 L1152,540 L1152,0 Z" fill="var(--white)"/>
    <g fill="none" stroke="var(--line)" stroke-width="2">
      <path d="M505,113 A145,145 0 0 1 505,403"/>
      <polyline points="561,130 569,90 625,82"/>
      <line x1="627" y1="197" x2="671" y2="190"/>
      <line x1="641" y1="273" x2="710" y2="273"/>
      <line x1="611" y1="348" x2="671" y2="355"/>
      <polyline points="561,391 569,429 625,436"/>
    </g>
    <g fill="var(--white)" stroke="var(--line)" stroke-width="2">
      <circle cx="561" cy="130" r="8"/><circle cx="627" cy="197" r="8"/>
      <circle cx="641" cy="273" r="8"/><circle cx="611" cy="348" r="8"/>
      <circle cx="561" cy="391" r="8"/>
    </g>
    <circle cx="497" cy="258" r="128" fill="#e6ebf2"/>
    <circle cx="497" cy="258" r="114" fill="var(--white)" filter="url(#soft2)"/>
    <circle cx="428" cy="257" r="10" fill="var(--brand)"/>
    <text class="brand-name" x="446" y="269" font-size="34">Orbita</text>
  </svg>

  <article class="module module--deep" style="left:625px;top:29px">
    <div class="module__icon" style="background:var(--icon-teal)">
      <svg viewBox="0 0 44 44" fill="#fff"><circle cx="22" cy="14" r="6"/><path d="M12,34 q0,-14 10,-14 q10,0 10,14 z"/><circle cx="10" cy="18" r="4.5"/><path d="M2,33 q0,-11 8,-11 q4,0 5,3 l-3,8 z"/><circle cx="34" cy="18" r="4.5"/><path d="M42,33 q0,-11 -8,-11 q-4,0 -5,3 l3,8 z"/></svg>
    </div>
    <div><h3>Nómina</h3><p>Automatice los cálculos de la nómina para salarios, deducciones, impuestos y otras formas de compensación, en base a la legislación del país.</p></div>
  </article>

  <article class="module module--bright" style="left:671px;top:128px">
    <div class="module__icon" style="background:var(--icon-yellow)">
      <svg viewBox="0 0 44 44" fill="#fff"><path d="M22,5 a12,12 0 0 1 7,21.5 v4.5 h-14 v-4.5 a12,12 0 0 1 7,-21.5 z"/><rect x="15" y="33" width="14" height="3" rx="1"/><rect x="17" y="37.5" width="10" height="3" rx="1.5"/></svg>
    </div>
    <div><h3>Asistencia</h3><p>Monitorea y genere registros de horas por cada empleado, en los que se incluye la fecha de inicio y de finalización de cada tarea.</p></div>
  </article>

  <article class="module module--soft" style="left:710px;top:227px">
    <div class="module__icon" style="background:var(--icon-orange)">
      <svg viewBox="0 0 44 44" fill="#fff"><rect x="6" y="8" width="3.5" height="28"/><rect x="6" y="33" width="32" height="3.5"/><rect x="13" y="23" width="4" height="8"/><rect x="19" y="17" width="4" height="14"/><rect x="25" y="20" width="4" height="11"/><rect x="31" y="12" width="4" height="19"/></svg>
    </div>
    <div><h3>Evaluación de Desempeño</h3><p>Alinee su mano de obra con los objetivos de la organización y de seguimiento a los indicadores clave de desempeño de los empleados.</p></div>
  </article>

  <article class="module module--bright" style="left:671px;top:327px">
    <div class="module__icon" style="background:var(--icon-violet)">
      <svg viewBox="0 0 44 44" fill="#fff"><circle cx="16" cy="24" r="10"/><circle cx="16" cy="24" r="4" fill="var(--icon-violet)"/><circle cx="32" cy="14" r="6"/><circle cx="32" cy="14" r="2.2" fill="var(--icon-violet)"/><circle cx="33" cy="32" r="5.5"/><circle cx="33" cy="32" r="2" fill="var(--icon-violet)"/></svg>
    </div>
    <div><h3>Contrataciones</h3><p>Optimize la contratación al simplificarla y hacerlo transparente, intuitivo e interactivo.</p></div>
  </article>

  <article class="module module--deep" style="left:625px;top:426px">
    <div class="module__icon" style="background:var(--icon-sky)">
      <svg viewBox="0 0 44 44"><rect x="8" y="9" width="28" height="20" rx="2" fill="none" stroke="#fff" stroke-width="3"/><path d="M3,31 h38 v3 a3,3 0 0 1 -3,3 h-32 a3,3 0 0 1 -3,-3 z" fill="#fff"/></svg>
    </div>
    <div><h3>Portal Auto Servicio</h3><p>Empodera a los empleados para que gestionen sus actividades referentes a la administración de RRHH.</p></div>
  </article>
</section>

</body>
</html>
```